Northern Summit Builders & Affiliates Redesigning our Look

We need stationary (letterhead, envelopes, notepads, invoicing templates, etc) that all coordinate. We are an commerial and residential exteriors construction company that operates 3 companies which all run exclusively, however, the compliment one another well.

Northern Summit Builders (this company installs exteriors on jobsites both residential and commercial)
Northern Summit Roofing & Building Supply (this company sells exterior building materials to homeowners and builders.)
Northern Summit Dumpster Services (This company delivers roll away dumpster cans to homeowners and builders)

Just a note: When I say we do exterior work. We do roofing, siding, stone, windows/doors, gutters, and decks.

We are looking for stationary that includes all three and keeps with our patriotic theme

Info on our firm:
Address: 2718 Tamarind Rd, Elkton MI 48512
Phone: 231-555-0172
Website: www.northernsummit-example.us

Target Market(s)

Our companies target market is vast. We work in the B2B space as well as with homeowner (retail customers). We are in the home and commercial buiding construction field. We specialized in exteriors. (Roofing, Siding, Stone, Windows, Doors, Decks, Gutters)

Industry/Entity Type

Construction

Colors
ec1f27
ffffff
0555a3

Requirements
Must have
• Would like to have a clean professional look with a patriotic theme
Nice to have
• Red/White/Blue

```html
<!DOCTYPE html>
<html lang="en">
<head>
<meta charset="utf-8">
<title>Northern Summit Builders — Stationery</title>
<link rel="stylesheet" href="https://fonts.googleapis.com/css2?family=Oswald:wght@400&family=Open+Sans:wght@400;600&display=swap">
<style>
  :root {
    --navy: #2c2c54;
    --red: #d1343a;
    --paper: #f7f7f7;
    --ink: #4a4a4a;
    --backdrop: #ececec;
    --rule: #8a8a8a;
  }
  * { box-sizing: border-box; margin: 0; padding: 0; }
  html, body { width: 1200px; height: 879px; overflow: hidden; }
  body {
    background: var(--backdrop);
    position: relative;
    font-family: "Open Sans", Arial, sans-serif;
    color: var(--ink);
  }
  .piece { position: absolute; background: var(--paper); }
  .wordmark {
    font-family: "Oswald", "Arial Narrow", sans-serif;
    font-weight: 400;
    line-height: 0.95;
    color: var(--navy);
    letter-spacing: -0.01em;
  }
  .wordmark--light { color: #f1f1f1; }
  .wordmark span { display: block; }
  .wordmark span + span { padding-left: 0.3em; }

  /* Letterhead */
  .letterhead { left: 254px; top: 111px; width: 326px; height: 462px; }
  .letterhead .wordmark { position: absolute; left: 22px; top: 24px; font-size: 17px; }
  .letterhead__footer {
    position: absolute; left: 22px; right: 24px; bottom: 17px;
    border-top: 1px solid var(--rule); padding-top: 6px;
    display: flex; justify-content: space-between; align-items: flex-end;
    font-size: 5px; line-height: 7.5px;
  }
  .contact-list { list-style: none; }
  .contact-list li { display: flex; align-items: center; gap: 3px; }
  .contact-list svg { width: 5px; height: 5px; fill: var(--navy); }
  .letterhead__address { text-align: right; }

  /* Folder */
  .folder { left: 635px; top: 89px; width: 387px; height: 486px; background: var(--navy); }
  .folder__spine { position: absolute; left: 0; top: 0; width: 20px; height: 100%; background: var(--red); }
  .folder .wordmark { position: absolute; left: 94px; top: 180px; font-size: 58px; }

  /* Business cards */
  .card { width: 147px; height: 84px; left: 136px; }
  .card--front { top: 613px; display: flex; align-items: center; padding: 0 8px 0 12px; }
  .card--front .wordmark { font-size: 13px; width: 58px; }
  .card__details {
    border-left: 1px solid #bbb; padding-left: 6px; margin-left: 6px;
    font-size: 3.6px; line-height: 5.4px;
  }
  .card__name { font-weight: 600; font-size: 5px; color: var(--navy); }
  .card__role { color: var(--red); margin-bottom: 2px; }
  .card--back { top: 720px; background: var(--navy); display: flex; flex-direction: column; align-items: center; justify-content: center; }
  .card--back .wordmark { font-size: 16px; margin-top: 4px; }
  .card__web { margin-top: 10px; font-size: 4.5px; letter-spacing: 0.2em; color: #e5e5e5; }

  /* Envelope front */
  .envelope-front { left: 321px; top: 625px; width: 366px; height: 175px; }
  .envelope-front .wordmark { position: absolute; left: 18px; top: 17px; font-size: 19px; }
  .envelope-front__address { position: absolute; left: 18px; top: 60px; font-size: 5px; }

  /* Envelope back */
  .envelope-back { left: 722px; top: 626px; width: 366px; height: 174px; }
  .envelope-back__flap { position: absolute; left: 0; top: 0; width: 100%; height: 60px; }
  .envelope-back .wordmark { position: absolute; left: 153px; top: 16px; font-size: 14px; }
</style>
</head>
<body>

  <section class="piece letterhead" aria-label="Letterhead">
    <div class="wordmark"><span>Northern</span><span>Summit</span></div>
    <footer class="letterhead__footer">
      <ul class="contact-list">
        <li><svg viewBox="0 0 10 10"><path d="M2 0h2l1 3-1.5 1a6 6 0 0 0 2.5 2.5L7 5l3 1v2a2 2 0 0 1-2 2A8 8 0 0 1 0 2a2 2 0 0 1 2-2z"/></svg>231-555-0172</li>
        <li><svg viewBox="0 0 10 10"><path d="M0 2h10v6H0z M0 2l5 3 5-3" /></svg>emarsh@northernsummit-example.us</li>
        <li><svg viewBox="0 0 10 10"><circle cx="5" cy="5" r="5"/></svg>www.northernsummit-example.us</li>
      </ul>
      <address class="letterhead__address" style="font-style:normal">2718 Tamarind Rd<br>Elkton MI 48512</address>
    </footer>
  </section>

  <section class="piece folder" aria-label="Presentation folder">
    <div class="folder__spine"></div>
    <div class="wordmark wordmark--light"><span>Northern</span><span>Summit</span></div>
  </section>

  <section class="piece card card--front" aria-label="Business card front">
    <div class="wordmark"><span>Northern</span><span>Summit</span></div>
    <div class="card__details">
      <div class="card__name">Evan Marsh</div>
      <div class="card__role">CEO/Founder</div>
      <div>2718 Tamarind Rd</div>
      <div>Elkton MI 48512</div>
      <div>231-555-0172</div>
      <div>emarsh@northernsummit-example.us</div>
      <div>www.northernsummit-example.us</div>
    </div>
  </section>

  <section class="piece card card--back" aria-label="Business card back">
    <div class="wordmark wordmark--light"><span>Northern</span><span>Summit</span></div>
    <div class="card__web">www.northernsummit-example.us</div>
  </section>

  <section class="piece envelope-front" aria-label="Envelope front">
    <div class="wordmark"><span>Northern</span><span>Summit</span></div>
    <div class="envelope-front__address">2718 Tamarind Rd, Elkton MI 48512</div>
  </section>

  <section class="piece envelope-back" aria-label="Envelope back">
    <svg class="envelope-back__flap" viewBox="0 0 366 60" preserveAspectRatio="none">
      <path d="M0 0H366V40L356 58H10L0 40Z" fill="var(--navy)"/>
    </svg>
    <div class="wordmark wordmark--light"><span>Northern</span><span>Summit</span></div>
  </section>

</body>
</html>
```